Volora Laundry and Dry Cleaning Poster

We need a Poster and Window Sticker for our Laundry and Dry cleaning shop (VOLORA LAUNDRY AND DRY CLEANING).
info we like on the design. Logo is included
Company Name: Volora Laundry and Dry Cleaning
Slogan: It Comes Back Clean
Location: Kwentu-Dasor, Accra
Working Hours: Mon-Sat 8am to 5pm
Tel: +233 30 781 6242
email:info@voloralaundry.example
website: www.voloralaundry.example
fb: fb.com/voloralaundry

Target Market(s)

Laundry Shop

Colors
33a6d7
9bcb3b

```html
<!DOCTYPE html>
<html lang="en">
<head>
<meta charset="utf-8">
<title>Volora Laundry and Dry Cleaning Poster</title>
<link href="https://fonts.googleapis.com/css2?family=Montserrat:wght@300;400;700;800;900&display=swap" rel="stylesheet">
<style>
  :root {
    --cyan: #33a6d7;
    --sky: #3dbfe8;
    --lime: #9bcb3b;
    --bright-lime: #8fe01a;
    --ink: #262a2b;
    --white: #ffffff;
    --foam: #79dcf0;
  }
  html, body {
    margin: 0;
    padding: 0;
    width: 1200px;
    height: 1007px;
    overflow: hidden;
    background: var(--white);
  }
  .poster {
    position: relative;
    width: 1200px;
    height: 1007px;
    background: var(--white);
    font-family: "Montserrat", Arial, sans-serif;
  }
  .poster > * { position: absolute; }

  /* left column */
  .side-band { left: 0; top: 0; width: 430px; height: 34px; background: var(--sky); }
  .brand-mark {
    left: 40px; top: 100px;
    display: flex; align-items: center; gap: 14px;
  }
  .brand-mark .dot {
    width: 104px; height: 104px; border-radius: 50%;
    background: var(--sky);
  }
  .brand-mark .name {
    color: var(--sky);
    font-weight: 700;
    line-height: 1;
  }
  .brand-mark .name .big { display: block; font-size: 62px; letter-spacing: 1px; }
  .brand-mark .name .small { display: block; font-size: 13.5px; margin-top: 6px; letter-spacing: 0.3px; }

  .info-panel {
    left: 0; top: 293px; width: 430px; height: 714px;
    background: var(--sky);
  }
  .info-list { margin: 0; padding: 72px 0 0 48px; color: var(--white); }
  .info-item { margin: 0 0 38px; }
  .info-item dt { font-weight: 800; font-size: 26px; line-height: 32px; }
  .info-item dd { margin: 0; font-weight: 300; font-size: 26px; line-height: 32px; }

  /* right column */
  .top-band { left: 456px; top: 0; width: 744px; height: 34px; background: var(--bright-lime); }
  .headline {
    left: 456px; top: 46px; width: 744px; margin: 0;
    text-align: center;
    color: var(--sky);
    font-weight: 900;
    font-size: 52px;
    line-height: 60px;
    letter-spacing: 0.5px;
  }
  .wave-art {
    left: 456px; top: 180px; width: 744px; height: 114px;
    background: linear-gradient(180deg, rgba(255,255,255,0) 0%, #d6f4f6 45%, var(--foam) 100%);
  }
  .photo {
    left: 456px; top: 294px; width: 744px; height: 322px;
    background: linear-gradient(160deg, #ececec 0%, #f2e6d0 35%, #f1d6d8 60%, #cde9df 80%, #e6e6e6 100%);
  }
  .mid-band { left: 456px; top: 616px; width: 744px; height: 14px; background: var(--bright-lime); }
  .slogan-panel {
    left: 456px; top: 630px; width: 744px; height: 308px;
    background: var(--ink); overflow: hidden;
  }
  .slogan {
    position: absolute; left: 22px; top: 66px; margin: 0;
    color: var(--white);
    font-weight: 800;
    font-size: 68px;
    line-height: 84px;
    letter-spacing: 0;
  }
  .shirt-art {
    position: absolute; left: 552px; top: 24px; width: 174px; height: 200px;
    background: #f4f4f4; border-radius: 10px;
  }
  .corner-art {
    position: absolute; right: 0; bottom: 0; width: 150px; height: 160px;
    background: radial-gradient(circle at 100% 100%, #4fc7ee 0%, #1f7fd8 55%, rgba(31,127,216,0) 72%);
  }
  .footer-mark {
    position: absolute; left: 24px; top: 248px;
    display: flex; align-items: center; gap: 8px;
    color: var(--sky); font-weight: 700; font-size: 26px; line-height: 1;
  }
  .footer-mark .dot { width: 38px; height: 38px; border-radius: 50%; background: var(--sky); }
  .bottom-band { left: 456px; top: 948px; width: 744px; height: 59px; background: var(--bright-lime); }
</style>
</head>
<body>
<main class="poster">
  <div class="side-band"></div>
  <div class="brand-mark">
    <span class="dot"></span>
    <span class="name"><span class="big">Volora</span><span class="small">LAUNDRY AND DRY CLEANING</span></span>
  </div>

  <section class="info-panel">
    <dl class="info-list">
      <div class="info-item"><dt>Location:</dt><dd>Kwentu-Dasor, Accra</dd></div>
      <div class="info-item"><dt>Working hours:</dt><dd>Mon-Sat 8am to 5pm</dd></div>
      <div class="info-item"><dt>Telephone:</dt><dd>+233-30-781-6242</dd></div>
      <div class="info-item"><dt>email:</dt><dd>info@voloralaundry.example</dd></div>
      <div class="info-item"><dt>website:</dt><dd>www.voloralaundry.example</dd></div>
      <div class="info-item"><dt>Facebook:</dt><dd>fb.com/voloralaundry</dd></div>
    </dl>
  </section>

  <div class="top-band"></div>
  <h1 class="headline">VOLORA LAUNDRY AND<br>DRY CLEANING</h1>

  <div class="wave-art" role="img" aria-label="Decorative cyan and lime wave with floating soap bubbles"></div>

  <div class="photo" role="img" aria-label="Photo from above of a woman in a yellow top ironing a pink shirt beside a stack of folded clothes"></div>
  <div class="mid-band"></div>

  <section class="slogan-panel">
    <p class="slogan">IT COMES<br>BACK CLEAN</p>
    <div class="shirt-art" role="img" aria-label="Illustration of a clean white T-shirt on a hanger"></div>
    <div class="corner-art" role="img" aria-label="Decorative blue corner swoosh with small bubbles"></div>
    <div class="footer-mark"><span class="dot"></span><span>Volora</span></div>
  </section>

  <div class="bottom-band"></div>
</main>
</body>
</html>
```